Poster for a Vegetarian Food Truck/Restaurant

Ours is a food truck with lots of greens in the menu. The name of our restaurant is Plum Nibbles.

I want to create a Poster image for the restaurant. Please submit designs on any one or both the themes described below

Size: 1.6 meters by 4.6 meters (horizontal)

Design Theme #1
A poster based off 'Newspaper front page'.
The poster should look like the front page of a newspaper with 'Plum Nibbles' as its name. The Plum Nibbles should appear prominently (in green color, possibly light green or lemon color). The poster will have a few snippets about benefits of certain food items or some trivia along with an image. For example 'Garlic is high in minerals & vitamins', 'Chickpeas are high on fiber'. I'll decide on the exact text meanwhile.

I have attached 2 sample images to give an idea.

Design Theme #2

It should consist of the following 3 components:
1. Green Forest like back ground
2. Image of a chef with a welcoming, smiling face
3. The text 'Plum Nibbles' should appear in the poster

I want Tobin Marsh lookalike, the main character from the animation movie 'Sunny Days over Dumpling Hill' to be the chef placed in the poster.
The chef should appear confident, smiling, young with his typical hair style

A sample picture of tobin marsh is attached in the brief

Target Market(s)

The poster will be pasted on a food truck

Industry/Entity Type

Restaurant

Requirements
Must have
• Poster with light but high resolution image(s)
• Attention to detail
Should not have
• The poster should not have dense/dark colors

```html
<!DOCTYPE html>
<html lang="en">
<head>
<meta charset="utf-8">
<title>Plum Nibbles – Poster</title>
<link href="https://fonts.googleapis.com/css2?family=Courgette&family=Crimson+Text:ital@0;1&family=Dancing+Script:wght@500&family=Fjalla+One&family=Josefin+Sans:wght@300;400;600&family=Cabin:ital,wght@1,700&family=Oswald:wght@300&display=swap" rel="stylesheet">
<style>
  :root {
    --page-bg: #d9d5c4;
    --paper: #ffffff;
    --olive: #a9b065;
    --lime: #b6c93a;
    --sage: #c6cab0;
    --garlic-olive: #b2ad63;
    --ink-grey: #6b6b6b;
    --soft-grey: #8f8f8f;
    --rule: #cfcfcf;
  }
  * { margin: 0; padding: 0; box-sizing: border-box; }
  html, body { width: 1200px; height: 849px; overflow: hidden; }
  body { background: var(--page-bg); position: relative; }

  .poster {
    position: absolute; left: 40px; top: 226px;
    width: 1120px; height: 396px;
    background: var(--paper);
  }
  .poster > * { position: absolute; }

  .chickpea-panel { left: 15px; top: 18px; width: 169px; height: 365px; background: var(--olive); }
  .chickpea-photo { left: 24px; top: 27px; width: 149px; height: 139px;
    background: linear-gradient(160deg, #f4f4f4, #b9b9b9); }
  .chickpea-fact { left: 15px; top: 182px; width: 169px; text-align: center;
    font-family: "Courgette", cursive; color: #fff; font-size: 28px; line-height: 47px; }

  .lime-fact { left: 203px; top: 24px; width: 120px; text-align: center;
    font-family: "Crimson Text", serif; font-style: italic; color: var(--soft-grey);
    font-size: 21px; line-height: 40.5px; }
  .lime-photo { left: 204px; top: 272px; width: 112px; height: 112px; border-radius: 50%;
    background: radial-gradient(circle at 45% 45%, #eef7a6, #bcd83a 60%, #8fb021); }

  .divider { width: 1px; background: var(--rule); }
  .divider-a { left: 343px; top: 18px; height: 365px; }
  .divider-b { left: 783px; top: 167px; height: 216px; }
  .divider-c { left: 934px; top: 161px; height: 222px; }

  .avocado-photo { left: 367px; top: 24px; width: 133px; height: 131px;
    border-radius: 50% 50% 46% 46%;
    background: radial-gradient(circle at 60% 65%, #d8df6a, #6f7a24 55%, #3c4114); }
  .avocado-title { left: 458px; top: 22px; width: 301px;
    font-family: "Josefin Sans", sans-serif; color: #333; font-weight: 600; }
  .avocado-title .small { display: block; font-size: 18px; letter-spacing: 2px; }
  .avocado-title .big { display: block; font-size: 21px; letter-spacing: 2.4px; text-align: right; margin-top: -2px; }
  .avocado-tagline { left: 514px; top: 84px; width: 245px; text-align: right;
    font-family: "Josefin Sans", sans-serif; font-weight: 300; color: var(--soft-grey);
    font-size: 18px; letter-spacing: 9px; line-height: 37px; }

  .rule { height: 1px; background: var(--rule); }
  .rule-top { left: 509px; top: 156px; width: 250px; }
  .rule-bottom { left: 367px; top: 274px; width: 392px; }

  .brand-name { left: 360px; top: 176px; width: 406px; text-align: center;
    font-family: "Fjalla One", sans-serif; color: var(--lime);
    font-size: 74px; line-height: 86px; letter-spacing: 1px; }

  .cucumber-fact { left: 369px; top: 286px; width: 295px; height: 93px; border-radius: 10px;
    background: var(--sage); color: #fff; text-align: center;
    font-family: "Dancing Script", cursive; font-size: 24px; line-height: 36px; padding-top: 10px; }
  .cucumber-photo { left: 677px; top: 303px; width: 82px; height: 64px; border-radius: 50%;
    background: radial-gradient(circle, #eaf5c2, #9cc23d 65%, #4f7a1a); }

  .garlic-photo { left: 783px; top: 30px; width: 157px; height: 113px; border-radius: 45%;
    background: radial-gradient(circle at 50% 55%, #ffffff, #d9d9d9 60%, #a9a9a9); }
  .garlic-fact { left: 800px; top: 168px; width: 114px; text-align: center;
    font-family: "Crimson Text", serif; color: var(--garlic-olive); line-height: 1; }
  .garlic-fact span { display: block; }
  .garlic-fact .l1, .garlic-fact .l2 { font-size: 31px; transform: scaleX(0.82); margin-bottom: 6px; }
  .garlic-fact .l3 { font-size: 44px; letter-spacing: 5px; margin: 2px 0 8px; }
  .garlic-fact .l4, .garlic-fact .l6 { font-size: 23px; transform: scaleX(0.85); }
  .garlic-fact .l5 { font-size: 30px; margin: 4px 0; }

  .leaf-stripes { left: 952px; top: 20px; width: 36px; height: 138px; }
  .leaf-heading { left: 990px; top: 16px; width: 112px; text-align: right;
    font-family: "Cabin", sans-serif; font-style: italic; font-weight: 700;
    color: var(--ink-grey); font-size: 35px; line-height: 44px; }
  .leaf-label { left: 952px; top: 160px; width: 151px; display: flex; justify-content: space-between;
    font-family: "Oswald", sans-serif; font-weight: 300; font-size: 9px; color: #333; }
  .lettuce-photo { left: 952px; top: 179px; width: 151px; height: 202px;
    background: radial-gradient(circle at 40% 40%, #e8f79c, #a6d33a 55%, #5f8c1c); }
</style>
</head>
<body>
  <main class="poster">
    <div class="chickpea-panel"></div>
    <div class="chickpea-photo" role="img" aria-label="Photo of chickpeas in white bowls"></div>
    <p class="chickpea-fact">Chickpeas<br>are<br>high<br>on fiber</p>

    <p class="lime-fact">Lime is<br>high in<br>vitamin C<br>and it<br>improves<br>digestion</p>
    <div class="lime-photo" role="img" aria-label="Photo of a halved lime"></div>

    <div class="divider divider-a"></div>

    <div class="avocado-photo" role="img" aria-label="Photo of a whole and halved avocado"></div>
    <h2 class="avocado-title"><span class="small">THE</span><span class="big">AMAZING AVOCADO</span></h2>
    <p class="avocado-tagline">RICH,CREAMY<br>&amp; FLAVORFUL</p>
    <div class="rule rule-top"></div>

    <h1 class="brand-name">PLUM NIBBLES</h1>
    <div class="rule rule-bottom"></div>

    <p class="cucumber-fact">Cucumbers are usually<br>more than 90% water.</p>
    <div class="cucumber-photo" role="img" aria-label="Photo of cucumber slices"></div>

    <div class="divider divider-b"></div>

    <div class="garlic-photo" role="img" aria-label="Photo of garlic bulbs and cloves"></div>
    <p class="garlic-fact"><span class="l1">GARLIC</span><span class="l2">IS HIGH</span><span class="l3">IN</span><span class="l4">MINERALS</span><span class="l5">&amp;</span><span class="l6">VITAMINS</span></p>

    <div class="divider divider-c"></div>

    <svg class="leaf-stripes" viewBox="0 0 36 138" aria-hidden="true">
      <g stroke="#b6c93a" stroke-width="1.4">
        <line x1="2" y1="0" x2="2" y2="138"/><line x1="7" y1="0" x2="7" y2="138"/>
        <line x1="12" y1="0" x2="12" y2="138"/><line x1="17" y1="0" x2="17" y2="138"/>
        <line x1="22" y1="0" x2="22" y2="138"/><line x1="27" y1="0" x2="27" y2="138"/>
        <line x1="32" y1="0" x2="32" y2="138"/>
      </g>
    </svg>
    <h2 class="leaf-heading">Raw<br>green<br>leaf</h2>
    <p class="leaf-label"><span>T</span><span>H</span><span>E</span><span>&nbsp;</span><span>B</span><span>E</span><span>N</span><span>E</span><span>F</span><span>I</span><span>T</span><span>S</span></p>
    <div class="lettuce-photo" role="img" aria-label="Photo of fresh green lettuce leaves"></div>
  </main>
</body>
</html>
```